Venture firm needs flyer to attract Sales Professionals as Advisors

Creation of either a pdf Flyer or Brochure.
The target audience are senior sales professionals of the Information Technology industry. The flyer needs to come across highly professional, business oriented, positive. Text for the brochure is attached. The colors/graphics should align with Tormid Ventures corporate appearance: www.tormid-example.ventures

Target Market(s)

Sales Professionals in the Information Technology Industry

Industry/Entity Type

Information Technology

Font styles to use
Other font styles liked:
• Raleway

Requirements
Must have
• fitting the corporate look and feel: www.tormid-example.ventures

```html
<!DOCTYPE html>
<html lang="en">
<head>
<meta charset="utf-8">
<title>Tormid Sales Council – Flyer</title>
<link rel="stylesheet" href="https://fonts.googleapis.com/css2?family=Montserrat:wght@500;600;700&family=Raleway:wght@500;600&family=Questrial&display=swap">
<style>
  :root {
    --page-bg: #e8e8e6;
    --navy: #0f3a60;
    --navy-text: #163f66;
    --ink: #111;
    --grey: #3a3a3a;
    --white: #fff;
    --icon: #4f7fb5;
  }
  * { margin: 0; padding: 0; box-sizing: border-box; }
  html, body { width: 1200px; height: 1200px; overflow: hidden; background: var(--page-bg); }
  .flyer {
    position: absolute; left: 174px; top: 20px;
    width: 852px; height: 1160px; overflow: hidden;
    font-family: "Raleway", sans-serif;
  }
  .flyer-bg { position: absolute; inset: 0; }
  .brand {
    position: absolute; left: 21px; top: 38px;
    font-family: "Questrial", sans-serif; font-size: 34px; letter-spacing: 1px;
    color: var(--white); font-weight: 400;
  }
  .title {
    position: absolute; right: 21px; top: 58px; text-align: right;
    font-family: "Montserrat", sans-serif; font-weight: 600;
    font-variant: small-caps; color: var(--navy-text);
    font-size: 48px; line-height: 40px; letter-spacing: 1px;
  }
  .title .abbr { display: block; font-size: 25px; line-height: 38px; color: var(--grey); font-variant: normal; padding-right: 8px; }
  .intro {
    position: absolute; right: 22px; text-align: right;
    font-size: 16.5px; line-height: 22px; font-weight: 600; color: var(--ink);
  }
  .intro-1 { top: 250px; width: 325px; }
  .intro-2 { top: 442px; width: 462px; }
  .intro-3 { top: 546px; width: 500px; }
  .section-title {
    position: absolute; top: 650px; left: 130px; right: 0; height: 54px;
    text-align: center; line-height: 54px; padding-left: 70px;
    font-family: "Montserrat", sans-serif; font-weight: 700; font-variant: small-caps;
    font-size: 34px; letter-spacing: 1px; color: var(--white);
  }
  .how-text {
    position: absolute; right: 380px; top: 740px; width: 465px; text-align: right;
    font-size: 16px; line-height: 28px; font-weight: 500; color: var(--navy-text);
  }
  .how-text p + p { margin-top: 6px; }
  .role { position: absolute; color: var(--navy-text); }
  .role-associates { top: 706px; left: 505px; width: 335px; }
  .role-advisors { top: 878px; left: 497px; width: 340px; }
  .role-head { display: flex; align-items: center; gap: 12px; margin-bottom: 4px; }
  .role-head h3 {
    font-family: "Montserrat", sans-serif; font-weight: 700; font-variant: small-caps;
    font-size: 19px; padding-top: 8px;
  }
  .role-associates .role-head { margin-left: 16px; }
  .role-advisors .role-head { margin-left: 12px; }
  .role ul { list-style: none; }
  .role li {
    position: relative; padding-left: 16px;
    font-size: 13.5px; line-height: 21px; font-weight: 600;
  }
  .role li::before { content: "»"; position: absolute; left: 0; top: 0; }
  .footer-band {
    position: absolute; left: 0; right: 0; bottom: 0; height: 58px;
    background: var(--navy); color: var(--white);
    display: flex; align-items: center; justify-content: center; text-align: center;
    font-family: "Montserrat", sans-serif; font-weight: 600; font-variant: small-caps;
    font-size: 14px; line-height: 21px; letter-spacing: 0.3px;
  }
</style>
</head>
<body>
<main class="flyer">
  <svg class="flyer-bg" width="852" height="1160" viewBox="0 0 852 1160">
    <defs>
      <linearGradient id="panel" x1="1" y1="0" x2="0" y2="1">
        <stop offset="0" stop-color="#dde6f1"/>
        <stop offset="1" stop-color="#b9cbe2"/>
      </linearGradient>
      <linearGradient id="sky" x1="0" y1="0" x2="0" y2="1">
        <stop offset="0" stop-color="#2d6bb1"/>
        <stop offset="0.65" stop-color="#5a91cf"/>
        <stop offset="0.8" stop-color="#c9d8ea"/>
        <stop offset="1" stop-color="#3d5f8c"/>
      </linearGradient>
    </defs>
    <rect width="852" height="1160" fill="url(#panel)"/>
    <polygon points="0,0 676,0 0,873" fill="url(#sky)" role="img" aria-label="Photo: paraglider with a yellow wing in a clear blue sky above snow-covered mountain peaks"/>
    <polygon points="173,650 852,650 852,704 130,704" fill="var(--navy)"/>
  </svg>

  <div class="brand">TORMID VENTURES</div>

  <h1 class="title">Tormid<br>Sales<br>Council<span class="abbr">(TSC)</span></h1>

  <p class="intro intro-1">The TSC is a by invitation only global community of high caliber Sales Professionals in the IT industry. Participating in the TSC provides significant wealth creation opportunities by earning consulting fees and sales commission or finding an exciting startup to work for.</p>
  <p class="intro intro-2">TSC members actively collaborate with each other to close deals, generate leads &amp; opportunities, navigate through client organizations and build a true advisory status with customers.</p>
  <p class="intro intro-3">TSC members get early first hand visibility into the latest technology innovations and learn how those technologies could assist their clients in solving their complex business objectives.</p>

  <h2 class="section-title">How it works</h2>

  <div class="how-text">
    <p>TSC members will be introduced to Tormid Ventures’ client and portfolio companies. This unique ability to learn about latest technology innovation keeps the participants up to date with industry trends and could open interesting earning or employment opportunities.</p>
    <p>Once exposed to a specific vendor, TSC members can decide if and how they would like to get further involved. Dependent on the interest level for the specific technology, the ability to offer a solution to a known customer problem or the sheer interest to develop new business, TSC members can participate in two ways:</p>
  </div>

  <section class="role role-associates">
    <div class="role-head">
      <svg width="44" height="44" viewBox="0 0 50 50" aria-hidden="true">
        <circle cx="25" cy="25" r="24" fill="var(--icon)"/>
        <circle cx="25" cy="25" r="20" fill="none" stroke="#fff" stroke-width="1.5"/>
        <circle cx="16" cy="17" r="3" fill="#fff"/><rect x="13" y="21" width="6" height="13" rx="2" fill="#fff"/>
        <circle cx="25" cy="15" r="3.4" fill="#fff"/><rect x="21.5" y="20" width="7" height="16" rx="2" fill="#fff"/>
        <circle cx="34" cy="17" r="3" fill="#fff"/><rect x="31" y="21" width="6" height="13" rx="2" fill="#fff"/>
      </svg>
      <h3>As Associates</h3>
    </div>
    <ul>
      <li>Associates are actively selling and promoting one or more Tormid Ventures´ portfolio companies.</li>
      <li>This could be an employment or a freelance opportunity.</li>
    </ul>
  </section>

  <section class="role role-advisors">
    <div class="role-head">
      <svg width="44" height="44" viewBox="0 0 50 50" aria-hidden="true">
        <circle cx="25" cy="25" r="24" fill="var(--icon)"/>
        <rect x="22" y="10" width="17" height="11" rx="2" fill="#fff"/>
        <polygon points="25,21 24,26 29,21" fill="#fff"/>
        <circle cx="19" cy="25" r="4.5" fill="#fff"/>
        <path d="M10 40 Q10 31 19 31 Q28 31 28 40 Z" fill="#fff"/>
      </svg>
      <h3>As Advisors</h3>
    </div>
    <ul>
      <li>Advisors offer their contacts and knowledge about customers to Associates.</li>
      <li>Advisors could create leads, support with introductions, explain customer organization and processes etc.</li>
      <li>They will be compensated by Associates with a pre-negotiated % of commission of a future sale that was supported by the Advisor.</li>
    </ul>
  </section>

  <footer class="footer-band">Whatever level of involvement a TSC member seeks there is plenty of opportunity to be rewarded for<br>working with fellow Sales Professionals and Great Startups on the forefront of technical innovation.</footer>
</main>
</body>
</html>
```